Thrifty Haul: Junk Removal - Website Design

We need a design and uploaded to Hostivra.com. I enclosed our postcard for reference too. I need a contact from at the top right so I can get leads.

Here are the sites I like:

https://trykemvan.com/
https://www.1800zibwaste.com
https://www.brindlemoversclearingco.com/junk-removal/
http://anookforgrams.com/
http://www.drivelunt.com/alternate/
https://www.servicevangifting.org/
http://www.autosforpatriots.org/indexj/

Coding

Coded - Design and coding required

Number of Pages Required

1 page

```html
<!DOCTYPE html>
<html lang="en">
<head>
<meta charset="utf-8">
<title>Thrifty Haul – Junk Removal</title>
<link href="https://fonts.googleapis.com/css2?family=Montserrat:wght@400;500;600;700;800&display=swap" rel="stylesheet">
<style>
:root{
  --blue:#0c4697;
  --blue-deep:#0a3d85;
  --green:#8cc63f;
  --green-dark:#79b52c;
  --ink:#222;
  --muted:#555;
  --pale:#f0f4f8;
  --footer:#2a2627;
  --white:#fff;
}
*{box-sizing:border-box;margin:0;padding:0}
html,body{width:1200px;height:3232px;overflow:hidden}
body{font-family:'Montserrat',sans-serif;color:var(--ink);position:relative;background:var(--white)}
.abs{position:absolute}
section,header,footer,nav.navbar{position:absolute;left:0;width:1200px;overflow:hidden}
.center{text-align:center;left:0;width:1200px}

/* top bar */
.topbar{top:0;height:75px;background:var(--blue)}
.brand{left:237px;top:20px;font-weight:800;font-size:29px;color:var(--green);letter-spacing:.5px}
.icon-circle{width:32px;height:32px;border-radius:50%;background:#3a66a8;display:flex;align-items:center;justify-content:center}
.top-email{left:624px;top:30px;color:var(--white);font-size:11px}
.top-service{left:804px;top:21px;font-size:9.5px;color:var(--white);font-weight:600;width:160px;text-align:center}
.top-call{left:804px;top:35px;font-size:16px;color:var(--green);font-weight:700;width:160px;text-align:center}

/* nav */
.navbar{top:75px;height:32px;background:var(--white);box-shadow:0 1px 3px rgba(0,0,0,.08);overflow:visible!important;z-index:2}
.nav{left:237px;top:0;display:flex;height:32px;align-items:center;font-size:10px;font-weight:500;color:#333;letter-spacing:.3px}
.nav a{color:inherit;text-decoration:none;padding:0 15px}
.nav a.active{color:var(--blue);position:relative}
.nav a.active::before{content:"";position:absolute;left:0;right:0;top:-10px;height:3px;background:var(--green)}
.nav .sep{color:#444}
.btn-green{background:var(--green);color:var(--white);font-weight:600;border-radius:18px;display:flex;align-items:center;justify-content:center}
.nav-btn{left:808px;top:-2px;width:153px;height:35px;font-size:13px}

/* hero */
.hero{top:107px;height:467px}
.hero-photo{left:0;top:0;width:1200px;height:467px;background:linear-gradient(100deg,#c9def2 0%,#a9cbeb 40%,#d9d3c4 60%,#b89a72 75%,#3b6fc4 90%)}
.hero h1{left:238px;top:162px;font-size:39px;font-weight:800;line-height:1.05;color:var(--blue)}
.hero h1 span{color:var(--green);display:block}
.hero-sub{left:238px;top:265px;font-size:12px;line-height:1.5;color:#222}
.offer{left:737px;top:87px;width:294px;height:294px;border-radius:50%;background:var(--blue)}
.offer-save{left:0;width:294px;top:24px;text-align:center;color:var(--white);font-size:30px;font-weight:400}
.offer-save sup{font-size:14px}
.offer-line{left:0;width:294px;top:62px;text-align:center;color:var(--green);font-weight:700;font-size:15px}
.offer-note{left:0;width:294px;top:83px;text-align:center;color:var(--white);font-size:7.5px}
.field{background:var(--white);border-radius:15px;height:30px;font-size:9.5px;color:#777;padding-left:17px;display:flex;align-items:center;position:absolute}
.offer .field{left:53px;width:188px}
.chev{position:absolute;right:14px;top:11px}
.offer-btn{position:absolute;left:53px;top:262px;width:188px;height:30px;font-size:9.5px;letter-spacing:.5px;border-radius:15px}

/* steps */
.steps{top:574px;height:274px;background:var(--pale)}
.steps h2{top:62px;font-size:15px;font-weight:700;color:var(--blue)}
.step{width:220px;text-align:center;top:115px}
.step svg{display:block;margin:0 auto 10px}
.step p{font-size:12px;line-height:1.5;color:#333;letter-spacing:.3px}

/* about */
.about{top:848px;height:462px;background:var(--white)}
.about-photo{left:237px;top:63px;width:338px;height:338px;border-radius:50%;background:radial-gradient(circle at 40% 45%,#c89c84 0%,#4f7fd0 35%,#2a5bb0 60%,#3b3f4a 100%)}
.about-title{left:626px;top:115px;font-size:29px;font-weight:800;color:var(--blue)}
.about-lead{left:626px;top:154px;width:340px;font-size:12px;line-height:1.5;color:#333}
.about-body{left:626px;top:205px;width:340px;font-size:9px;line-height:1.65;color:#555}
.btn-blue{left:626px;top:314px;width:100px;height:30px;background:var(--blue);color:var(--white);font-size:9px;font-weight:700;border-radius:15px;display:flex;align-items:center;justify-content:center;letter-spacing:.6px}

/* services */
.services{top:1310px;height:476px;background:linear-gradient(90deg,#0d3f86,#124c9c 50%,#0d3f86)}
.services h2{top:62px;font-size:22px;font-weight:700;color:var(--white)}
.services h2 span{color:var(--green)}
.services .sub{top:93px;font-size:11px;color:var(--white)}
.card{top:135px;width:226px;height:224px;background:var(--white);box-shadow:0 2px 6px rgba(0,0,0,.25)}
.card .img{height:175px;width:100%}
.card h3{text-align:center;font-size:15px;font-weight:700;margin-top:15px;color:#222}
.card h3.hl{color:var(--blue)}
.arrow{top:234px}
.btn-white{left:522px;top:392px;width:156px;height:30px;background:var(--white);color:var(--blue);font-size:9px;font-weight:700;border-radius:15px;display:flex;align-items:center;justify-content:center;letter-spacing:.6px}

/* why */
.why{top:1786px;height:267px;background:var(--green)}
.why h2{top:56px;font-size:23px;font-weight:700;color:#222}
.why h2 span{color:var(--blue)}
.why .sub{top:86px;font-size:11px;color:#222}
.feature{top:140px;width:180px;text-align:center}
.feature svg{display:block;margin:0 auto 8px}
.feature p{font-size:12px;line-height:1.5;color:#2a2a2a;letter-spacing:.3px}

/* testimonials */
.testimonials{top:2053px;height:371px;background:var(--white)}
.testimonials h2{top:61px;font-size:22px;font-weight:600;color:#222}
.avatar{left:330px;top:126px;width:132px;height:132px;border-radius:50%;background:radial-gradient(circle at 50% 40%,#e9c2aa 0%,#b48466 45%,#6b5142 75%,#3e3434 100%)}
.quote{left:489px;top:149px;width:390px;font-size:16px;line-height:1.4;color:#333}
.quote-name{left:489px;top:232px;font-size:11px;font-weight:600;letter-spacing:1.5px;color:var(--blue)}
.dots{left:568px;top:299px;display:flex;gap:5px}
.dots i{width:8px;height:8px;border-radius:50%;border:1px solid var(--green);display:block}
.dots i.on{background:var(--green)}

/* schedule */
.schedule{top:2424px;height:532px}
.schedule-photo{left:0;top:0;width:1200px;height:532px;background:linear-gradient(90deg,#a8b38f 0%,#d7c0a6 20%,#3a6cc4 35%,#e6e6e8 50%,#b58f63 70%,#2f5fb6 85%,#b28c60 100%)}
.sched-box{left:625px;top:63px;width:337px;height:405px;background:var(--blue)}
.sched-box h2{position:absolute;left:0;width:337px;text-align:center;top:33px;font-size:22px;font-weight:700;color:var(--white)}
.sched-box h2 span{color:var(--green)}
.sched-box .sub{position:absolute;left:0;width:337px;text-align:center;top:63px;font-size:11.5px;color:var(--white)}
.sched-box .field{width:138px}
.sched-box .area{height:74px;align-items:flex-start;padding-top:12px;width:287px}
.sched-btn{position:absolute;left:81px;top:338px;width:176px;height:36px;font-size:12px;border-radius:18px}

/* footer */
.footer{top:2956px;height:276px;background:var(--footer);color:var(--white)}
.f-h{font-size:11px;font-weight:600}
.f-t{font-size:9.5px;color:#bbb;line-height:1.6}
.f-call{font-size:15px;font-weight:700;color:var(--green)}
.social{display:flex;gap:7px;left:737px;top:126px}
.social i{width:24px;height:24px;border-radius:50%;border:1px solid #ccc;display:block}
.copy{left:237px;top:235px;font-size:8px;color:#ccc}
</style>
</head>
<body>

<header class="topbar">
  <div class="abs brand">THRIFTY HAUL</div>
  <div class="abs icon-circle" style="left:580px;top:22px">
    <svg width="14" height="11" viewBox="0 0 14 11" fill="none" stroke="#fff" stroke-width="1.2"><rect x="1" y="1" width="12" height="9" rx="1"/><path d="M1 1l6 5 6-5"/></svg>
  </div>
  <div class="abs top-email">info@thriftyhaul.com</div>
  <div class="abs icon-circle" style="left:761px;top:22px">
    <svg width="14" height="14" viewBox="0 0 14 14" fill="none" stroke="#fff" stroke-width="1.3"><path d="M2 8V7a5 5 0 0 1 10 0v1"/><rect x="1.5" y="8" width="3" height="4" rx="1"/><rect x="9.5" y="8" width="3" height="4" rx="1"/></svg>
  </div>
  <div class="abs top-service">24X7 Customer Service</div>
  <div class="abs top-call">Call: 1.800.555.0142</div>
</header>

<nav class="navbar">
  <div class="abs nav">
    <a class="active" href="#">HOME</a><span class="sep">I</span>
    <a href="#">ABOUT</a><span class="sep">I</span>
    <a href="#">SERVICES</a><span class="sep">I</span>
    <a href="#">TESTIMONIAL</a><span class="sep">I</span>
    <a href="#">CONTACT</a>
  </div>
  <div class="abs btn-green nav-btn">Schedule A Pickup</div>
</nav>

<section class="hero">
  <div class="abs hero-photo" role="img" aria-label="Masked removal worker carrying a cardboard box from a white van under a blue sky"></div>
  <h1 class="abs">No Contact<span>Junk Removal</span></h1>
  <p class="abs hero-sub">Online Booking + Safe touchless<br>pickups guaranteed!</p>
  <div class="abs offer">
    <div class="abs offer-save">Save <sup>$</sup>25</div>
    <div class="abs offer-line">On Your 1<sup style="font-size:8px">st</sup> Booking</div>
    <div class="abs offer-note">*Not valid on single item or minimum charge pickup.</div>
    <div class="field" style="top:107px">Your Name</div>
    <div class="field" style="top:145px">Email</div>
    <div class="field" style="top:183px">Phone</div>
    <div class="field" style="top:221px">Choose Service
      <svg class="chev" width="8" height="6" viewBox="0 0 8 6" fill="none" stroke="#888"><path d="M1 1l3 3 3-3"/></svg></div>
    <div class="btn-green offer-btn">BOOK ONLINE!</div>
  </div>
</section>

<section class="steps">
  <h2 class="abs center">All you have to do is point</h2>
  <div class="abs step" style="left:239px">
    <svg width="50" height="52" viewBox="0 0 50 52" fill="none" stroke="#222" stroke-width="1.6"><path d="M8 22h24v26H8z"/><path d="M12 22V10h16v12"/><path d="M14 14h12"/><path d="M12 30h16M12 36h16"/><circle cx="38" cy="42" r="8" fill="#8cc63f"/><path d="M36 8l6 6-8 8"/></svg>
    <p>House, Garage Estate<br>Cleanout</p>
  </div>
  <div class="abs step" style="left:490px">
    <svg width="46" height="52" viewBox="0 0 46 52" fill="none" stroke="#222" stroke-width="1.6"><rect x="2" y="2" width="42" height="48"/><path d="M2 30h42"/><rect x="8" y="8" width="30" height="18"/><path d="M6 36h8" stroke="#8cc63f" stroke-width="3"/></svg>
    <p>Furniture, Appliance<br>Removal</p>
  </div>
  <div class="abs step" style="left:740px">
    <svg width="50" height="52" viewBox="0 0 50 52" fill="none" stroke="#222" stroke-width="1.6"><path d="M4 8h30l-3 40H7z"/><path d="M2 8h34M14 4h10"/><path d="M12 16v24M19 16v24M26 16v24" stroke="#8cc63f" stroke-width="3"/><circle cx="38" cy="38" r="10" fill="#fff"/><path d="M34 36l4-4 4 4M38 32v10"/></svg>
    <p>We Recycling Your<br>Rubbish</p>
  </div>
</section>

<section class="about">
  <div class="abs about-photo" role="img" aria-label="Smiling removal worker in a blue cap carrying a rolled-up carpet"></div>
  <div class="abs about-title">THRIFTY HAUL</div>
  <p class="abs about-lead">We are full-service junk removal company serving areas across the united states. We're in your neighborhood.</p>
  <p class="abs about-body">Lorem ipsum dolor sit amet, consectetur adipiscing elit, sed do eiusmod tempor incididunt ut labore et dolore magna aliqua. Ut enim ad minim veniam, quis nostrud exercitation ullamco laboris nisi ut aliquip ex ea commodo consequat. Duis aute irure dolor in reprehenderit in voluptate velit esse cillum dolore eu fugiat nulla pariatur.</p>
  <div class="abs btn-blue">ABOUT US</div>
</section>

<section class="services">
  <h2 class="abs center">Full Service <span>Junk Removal</span></h2>
  <p class="abs center sub">Thrifty Haul is a full service junk removal company serving areas across the United States.</p>
  <svg class="abs arrow" style="left:192px" width="14" height="22" viewBox="0 0 14 22" fill="none" stroke="#fff" stroke-width="1.8"><path d="M12 2L3 11l9 9"/></svg>
  <svg class="abs arrow" style="left:992px" width="14" height="22" viewBox="0 0 14 22" fill="none" stroke="#fff" stroke-width="1.8"><path d="M2 2l9 9-9 9"/></svg>
  <div class="abs card" style="left:237px">
    <div class="img" role="img" aria-label="Cluttered room with boxes, bags and old furniture" style="background:linear-gradient(135deg,#6b4c33,#c7b59a 50%,#8a6a4c)"></div>
    <h3 class="hl">Residential</h3>
  </div>
  <div class="abs card" style="left:487px">
    <div class="img" role="img" aria-label="Two movers in blue uniforms lifting cardboard boxes" style="background:linear-gradient(135deg,#c45a3c,#2f62c2 45%,#c9a27a 80%)"></div>
    <h3>Moving</h3>
  </div>
  <div class="abs card" style="left:737px">
    <div class="img" role="img" aria-label="Scrap yard piled with crushed metal and old cars" style="background:linear-gradient(135deg,#8a8f97,#5b3f36 50%,#a14a2c)"></div>
    <h3>Commercial</h3>
  </div>
  <div class="abs btn-white">VIEW ALL SERVICES</div>
</section>

<section class="why">
  <h2 class="abs center">Why Choose <span>Thrifty Haul?</span></h2>
  <p class="abs center sub">America's Most Trusted name in Junk Removal</p>
  <div class="abs feature" style="left:228px">
    <svg width="30" height="30" viewBox="0 0 30 30" fill="none" stroke="#222" stroke-width="2"><circle cx="15" cy="15" r="12"/><path d="M15 8v7h5"/></svg>
    <p>On-time Junk Removal<br>Service</p>
  </div>
  <div class="abs feature" style="left:417px">
    <svg width="30" height="30" viewBox="0 0 30 30" fill="none" stroke="#222" stroke-width="2"><path d="M15 1v28M21 8c-1-2-3-3-6-3-4 0-6 2-6 4.5S11 13 15 14s7 2 7 5-3 5-7 5c-3 0-5-1-6-3"/></svg>
    <p>Up Front pricing, No<br>Hidden charges</p>
  </div>
  <div class="abs feature" style="left:603px">
    <svg width="30" height="30" viewBox="0 0 30 30" fill="none" stroke="#222" stroke-width="2"><path d="M4 7h22M11 7V3h8v4M7 7l2 21h12l2-21M12 12v12M15 12v12M18 12v12"/></svg>
    <p>Full-service Junk<br>Removal</p>
  </div>
  <div class="abs feature" style="left:792px">
    <svg width="30" height="30" viewBox="0 0 30 30" fill="none" stroke="#222" stroke-width="2"><circle cx="15" cy="15" r="12"/><circle cx="11" cy="11" r="1.5"/><circle cx="19" cy="12" r="1.5"/><circle cx="13" cy="19" r="1.5"/><circle cx="20" cy="19" r="1.5"/></svg>
    <p>Covid-19 Health and<br>Safety Complaint</p>
  </div>
</section>

<section class="testimonials">
  <h2 class="abs center">Customer Testimonials</h2>
  <div class="abs avatar" role="img" aria-label="Portrait photo of the reviewing customer"></div>
  <p class="abs quote">Cheap rates for furniture pick up. Great<br>service. Fast response time. Highly recommend<br>their services.</p>
  <div class="abs quote-name">- MARISA K</div>
  <div class="abs dots"><i class="on"></i><i></i><i></i><i></i><i></i></div>
</section>

<section class="schedule">
  <div class="abs schedule-photo" role="img" aria-label="Two smiling movers carrying a cardboard box beside a loaded van"></div>
  <div class="abs sched-box">
    <h2>Schedule A <span>Pickup</span></h2>
    <p class="sub">Get your junk removed today.</p>
    <div class="field" style="left:25px;top:107px">Your Name</div>
    <div class="field" style="left:175px;top:107px">Email</div>
    <div class="field" style="left:25px;top:151px">Phone</div>
    <div class="field" style="left:175px;top:151px">Date
      <svg class="chev" style="top:10px" width="9" height="9" viewBox="0 0 9 9" fill="none" stroke="#666"><rect x=".5" y="1.5" width="8" height="7"/><path d="M.5 4h8"/></svg></div>
    <div class="field" style="left:25px;top:195px">Choose Service
      <svg class="chev" width="8" height="6" viewBox="0 0 8 6" fill="none" stroke="#888"><path d="M1 1l3 3 3-3"/></svg></div>
    <div class="field" style="left:175px;top:195px">Zip Code</div>
    <div class="field area" style="left:25px;top:238px;border-radius:12px">Type your Message ...</div>
    <div class="btn-green sched-btn">Schedule A Pickup</div>
  </div>
</section>

<footer class="footer">
  <div class="abs f-h" style="left:237px;top:62px">24X7 Customer Service</div>
  <div class="abs f-call" style="left:237px;top:83px">Call Us: 1.800.555.0142</div>
  <div class="abs f-t" style="left:237px;top:103px;color:#ddd">e. info@thriftyhaul.com</div>
  <div class="abs f-t" style="left:237px;top:134px;color:#fff;font-weight:600">Location</div>
  <div class="abs f-t" style="left:237px;top:149px">412 Marlow Ave, Houston,<br>Texas 77010</div>

  <div class="abs f-h" style="left:489px;top:60px">Quick Link</div>
  <div class="abs f-t" style="left:489px;top:81px;line-height:2.2">Home<br>About<br>Services<br>Testimonial<br>Contact</div>

  <div class="abs f-h" style="left:737px;top:60px">Opening Hours</div>
  <div class="abs f-t" style="left:737px;top:81px">Monday to Friday<br>9am - 5pm</div>
  <div class="abs f-t" style="left:849px;top:81px">Saturday - Sunday:<br>Closed</div>
  <div class="abs social"><i></i><i></i><i></i><i></i><i></i></div>

  <div class="abs copy">© 2020 Thrifty Haul. All rights reserved</div>
</footer>

</body>
</html>
```